Young a vibrant Letting agent. New approach to the old market. our colors are various shades of green. We want a clean and clear design with our logo and beautiful shapes. Not too crowded but not too empty. Surprise us!

Size A5, (A4 folded in two)-Cover-Page2-Page3-Back Cover

Once the first and last page is designed, i will send you the content for page 2 and 3

```html
<!DOCTYPE html>
<html lang="en">
<head>
<meta charset="utf-8">
<title>Verdeo Lettings – A5 Brochure Spreads</title>
<link rel="stylesheet" href="https://fonts.googleapis.com/css2?family=Open+Sans:wght@400;600;700&display=swap">
<style>
  :root {
    --green: #8cc63f;
    --green-light: #a6d45a;
    --green-dark: #0f3d1e;
    --grey: #8a8a8a;
    --grey-box: #8f8f8f;
    --text-grey: #9a9a9a;
    --paper: #ffffff;
    --backdrop: #e8eae5;
  }
  * { box-sizing: border-box; margin: 0; padding: 0; }
  html, body {
    width: 1200px; height: 600px; overflow: hidden;
    background: var(--backdrop);
    font-family: "Open Sans", Arial, sans-serif;
  }
  .spread {
    position: absolute; top: 102px;
    width: 560px; height: 396px;
    background: var(--paper);
    display: flex;
    box-shadow: 0 4px 14px rgba(0,0,0,.18);
  }
  .spread--interior { left: 30px; }
  .spread--exterior { left: 610px; }
  .page { position: relative; width: 280px; height: 396px; overflow: hidden; }
  .page + .page { border-left: 1px solid #f0f0f0; }
  .page__shapes { position: absolute; inset: 0; width: 280px; height: 396px; }

  /* Page 2 */
  .intro-lead {
    position: absolute; left: 12px; top: 10px; width: 256px;
    color: var(--green); font-weight: 700; font-size: 7px; line-height: 1.3;
  }
  .intro-body {
    position: absolute; left: 12px; top: 44px; width: 256px;
    color: var(--text-grey); font-size: 6.4px; line-height: 1.35;
  }
  .promise-boxes {
    position: absolute; left: 12px; top: 76px; width: 256px;
    display: flex; gap: 6px;
  }
  .promise {
    flex: 1; border-radius: 20px; padding: 10px 10px;
    color: #fff; font-size: 7px; font-weight: 600; line-height: 1.35;
    text-align: justify; min-height: 92px;
  }
  .promise--green { background: var(--green); }
  .promise--grey { background: var(--grey-box); }
  .fee-note {
    position: absolute; left: 20px; width: 240px;
    color: var(--text-grey); font-size: 6.2px; line-height: 1.35; text-align: center;
  }
  .tagline {
    position: absolute; left: 0; width: 280px; text-align: center;
    color: var(--green); font-weight: 700; font-size: 8.6px;
  }
  .page--two .fee-note { top: 174px; }
  .page--two .tagline { top: 192px; }

  /* Page 3 */
  .placeholder-heading {
    position: absolute; top: 66px; left: 0; width: 280px; text-align: center;
    color: var(--grey); font-size: 11px;
  }
  .page--three .fee-note { top: 148px; }
  .page--three .tagline { top: 168px; }

  /* Logo stand-in */
  .brand { position: absolute; display: flex; flex-direction: column; align-items: center; }
  .brand__name {
    display: flex; align-items: center; gap: 5px;
    font-weight: 700; font-size: 13px; color: var(--green-dark);
  }
  .brand__mark { width: 8px; height: 8px; background: var(--green-dark); }
  .brand__web { font-size: 6.4px; font-weight: 600; color: var(--green-dark); margin-top: 3px; }
  .page--front .brand { right: 22px; top: 148px; }
  .page--back .brand { left: 0; width: 280px; top: 258px; }
  .page--back .brand__name { color: var(--green); }

  .contact {
    position: absolute; top: 296px; left: 0; width: 280px; text-align: center;
    font-size: 6.4px; font-weight: 600; color: var(--green-dark); line-height: 1.5;
  }
</style>
</head>
<body>

<!-- Interior spread: page 2 and page 3 -->
<section class="spread spread--interior">
  <article class="page page--two">
    <svg class="page__shapes" viewBox="0 0 280 396" aria-hidden="false">
      <defs>
        <linearGradient id="lounge-fire" x1="0" y1="0" x2="1" y2="1">
          <stop offset="0" stop-color="#d9d2c4"/>
          <stop offset=".5" stop-color="#b9ab95"/>
          <stop offset="1" stop-color="#8d7d66"/>
        </linearGradient>
      </defs>
      <path d="M0,212 H196 C224,212 226,238 254,238 H280 V330 H0 Z" fill="var(--green)"/>
      <path role="img" aria-label="Photo of a bright living room with a fireplace and white sofa"
            d="M16,222 H196 C222,222 224,248 252,248 H280 V396 H16 Z" fill="url(#lounge-fire)"/>
    </svg>
    <p class="intro-lead">By choosing Verdeo Lettings to market your property, you choose to save money. We , unlike other agents, work on a no let no fee basis, and do not charge for marketing your property.</p>
    <p class="intro-body">Instructing us to market your property would cost you nothing and you would only pay if the property is let by us. If you let it through other agents, we won't charge you a penny.</p>
    <div class="promise-boxes">
      <p class="promise promise--green">We will attend viewings 7 days from 8am until 9pm, as most tenants are working during the day and would find very convenient evening and weekends appointments</p>
      <p class="promise promise--grey">We will carefully choose a suitable tenant, do all referencing, credit checks and employment referencing. We would present you all information we have and it is your decision</p>
    </div>
    <p class="fee-note">If the property is let by us, once the tenancy agreement is signed, we would charge you a fee of £150+VAT.</p>
    <p class="tagline">"No percentage, no complicated contracts"</p>
  </article>

  <article class="page page--three">
    <svg class="page__shapes" viewBox="0 0 280 396">
      <defs>
        <linearGradient id="lounge-sofa" x1="0" y1="0" x2="1" y2="1">
          <stop offset="0" stop-color="#e3ddcf"/>
          <stop offset=".55" stop-color="#c8b89c"/>
          <stop offset="1" stop-color="#a08a6c"/>
        </linearGradient>
      </defs>
      <path d="M170,200 H280 V300 H200 C184,300 180,276 170,262 Z" fill="var(--green)"/>
      <path role="img" aria-label="Photo of a furnished living room with a cream sofa and window"
            d="M0,206 H206 V340 C206,370 186,388 160,388 H0 Z" fill="url(#lounge-sofa)"/>
    </svg>
    <h2 class="placeholder-heading">Your new info</h2>
    <p class="fee-note">If the property is let by us, once the tenancy agreement is signed, we would charge you a fee of £150+VAT.</p>
    <p class="tagline">"No percentage, no complicated contracts"</p>
  </article>
</section>

<!-- Exterior spread: front and back cover -->
<section class="spread spread--exterior">
  <article class="page page--front">
    <svg class="page__shapes" viewBox="0 0 280 396">
      <defs>
        <linearGradient id="cover-lounge" x1="0" y1="0" x2="1" y2="1">
          <stop offset="0" stop-color="#e5dfd2"/>
          <stop offset=".55" stop-color="#c9b99d"/>
          <stop offset="1" stop-color="#9c8668"/>
        </linearGradient>
      </defs>
      <path d="M0,22 H130 C158,22 160,60 190,60 H252 C268,60 272,72 272,88 V196 H0 Z" fill="var(--green)"/>
      <path role="img" aria-label="Photo of a furnished living room with a cream sofa"
            d="M0,206 H272 V300 C250,300 248,330 232,350 C220,368 206,380 186,380 H0 Z" fill="url(#cover-lounge)"/>
    </svg>
    <div class="brand">
      <span class="brand__name"><span class="brand__mark"></span>Verdeo Lettings</span>
      <span class="brand__web">www.verdeolets.co.uk</span>
    </div>
  </article>

  <article class="page page--back">
    <svg class="page__shapes" viewBox="0 0 280 396">
      <defs>
        <linearGradient id="terrace-street" x1="0" y1="0" x2="1" y2="1">
          <stop offset="0" stop-color="#8fa9c8"/>
          <stop offset=".45" stop-color="#9a4a34"/>
          <stop offset="1" stop-color="#5a3326"/>
        </linearGradient>
      </defs>
      <path d="M150,70 H200 C226,70 228,100 252,100 H280 V160 H150 Z" fill="var(--green)"/>
      <path role="img" aria-label="Photo of a brick terrace street with a to let sign"
            d="M4,14 H150 C168,14 172,30 172,46 V160 H4 Z" fill="url(#terrace-street)"/>
    </svg>
    <div class="brand">
      <span class="brand__name"><span class="brand__mark"></span>Verdeo Lettings</span>
    </div>
    <p class="contact">
      Northfield: 01632 960418<br>
      Eastbury: 0161 496 0732<br>
      Email: hello@verdeolets.co.uk<br>
      www.verdeolets.co.uk
    </p>
  </article>
</section>

</body>
</html>
```